Victorian Era general store concept

I want to design a Victorian era general store themed web site. I Have existing advertisements from the Harrowgate Courier from the 1850's that display the Trumbo and Kessler brand. I would like to create a logo with that and if the designer can add any anything to it that would enhance the look yet retain its classic Victorian appear that would be great. I will upload the Harrowgate courier publication. Look for Trumbo and Kessler ads on there. I would like the design to be simplistic yet classic. Nothing to busy. I would like to add the phrase "A puget sound orginal" "Est. 1851"
https://www.archivexa.example/library/papers/papers_detail.aspx?t=29
Updates

I am going to upload another file that is very clear. Trumbo and Kessler regular line of packets. Hopefully this will help.

Target Market(s)

Undetermined

Industry/Entity Type

Online Store

Number of Pages Required

1 page

Font styles to use
Other font styles liked:
• What is on the adds.

Colors

Designer to choose colors to be used in the design.

Requirements
Must have
• Puget Sound orginal and est 1851
• Any "Trumbo and Kessler" advertisement from the Harrowgate Courier with details thereof.
Nice to have
• Some type of ship in the logo would be nice if it fits well.

```html
<!DOCTYPE html>
<html lang="en">
<head>
<meta charset="utf-8">
<title>Trumbo &amp; Kessler — A Puget Sound Orginal</title>
<link rel="stylesheet" href="https://fonts.googleapis.com/css2?family=Didact+Gothic&family=Questrial&family=Libre+Baskerville:ital@1&display=swap">
<style>
  :root {
    --ink: #2b3542;
    --ink-soft: #7d8a9c;
    --mist-top: #d3d3d5;
    --mist-bottom: #f4f4f4;
    --card: #f4f4f4;
    --rule: #9a9a9c;
    --button: #3f4b5c;
    --about-bg: #252f3c;
    --about-title: #8e9bad;
    --testimonial-bg: #cfcfd0;
    --portrait: #5a5c60;
    --footer-bg: #111620;
    --white: #ffffff;
  }
  * { box-sizing: border-box; margin: 0; padding: 0; }
  html, body { width: 706px; height: 1200px; overflow: hidden; }
  body {
    position: relative;
    background: var(--mist-bottom);
    color: var(--ink);
    font-family: "Questrial", sans-serif;
  }
  .hero {
    position: absolute; left: 0; top: 0; width: 706px; height: 676px;
    background: linear-gradient(to bottom, var(--mist-top) 0%, #d0d0d2 40%, #dcdcdd 60%, var(--mist-bottom) 82%);
  }
  .hero-scene {
    position: absolute; left: 0; top: 150px; width: 706px; height: 330px;
    background: radial-gradient(ellipse 60% 45% at 50% 45%, rgba(150,150,154,0.35), rgba(150,150,154,0) 70%);
  }
  .brand {
    position: absolute; left: 189px; top: 44px; width: 300px; text-align: center;
    font-family: "Didact Gothic", sans-serif; color: var(--ink);
  }
  .brand-mark {
    display: block; width: 14px; height: 14px; margin: 0 auto 6px;
    border-radius: 50%; background: var(--ink);
  }
  .brand-name { font-size: 24px; letter-spacing: 0.5px; line-height: 1; }
  .brand-est { font-size: 12px; letter-spacing: 1.5px; margin-top: 3px; }
  .nav-rule { position: absolute; top: 124px; height: 2px; background: var(--rule); }
  .nav-rule.left { left: 0; width: 200px; }
  .nav-rule.right { left: 547px; width: 159px; }
  .nav a {
    position: absolute; font-family: "Didact Gothic", sans-serif;
    font-size: 16px; letter-spacing: 0.5px; text-decoration: none; line-height: 1;
  }
  .top-nav a { top: 117px; color: var(--ink); }
  .hero-title {
    position: absolute; left: 0; width: 678px; top: 225px; text-align: center;
    font-family: "Didact Gothic", sans-serif; font-weight: 400;
    font-size: 22px; letter-spacing: 0.3px; color: var(--ink);
  }
  .enquiry {
    position: absolute; left: 206px; top: 318px; width: 254px; height: 295px;
    background: var(--card); box-shadow: 0 3px 5px rgba(0,0,0,0.28);
  }
  .enquiry-title {
    position: absolute; left: 28px; top: 14px; font-weight: 400;
    font-family: "Didact Gothic", sans-serif; font-size: 21px; color: var(--ink);
  }
  .enquiry-title span { color: var(--ink-soft); }
  .field-label { position: absolute; font-size: 10.5px; color: var(--ink); }
  .field {
    position: absolute; background: var(--white); border: 1px solid var(--ink);
    font-family: "Questrial", sans-serif;
  }
  .submit {
    position: absolute; left: 168px; top: 244px; width: 58px; height: 21px;
    background: var(--button); color: var(--white); border: 0;
    font-family: "Questrial", sans-serif; font-size: 10px;
  }
  .about {
    position: absolute; left: 0; top: 676px; width: 706px; height: 182px;
    background: var(--about-bg); text-align: center;
  }
  .section-title {
    font-family: "Didact Gothic", sans-serif; font-weight: 400; font-size: 22px;
    letter-spacing: 0.3px;
  }
  .about .section-title { position: absolute; left: 0; width: 694px; top: 24px; color: var(--about-title); }
  .about-text {
    position: absolute; left: 97px; top: 66px; width: 518px;
    font-size: 10.6px; line-height: 13.8px; color: var(--white); font-weight: 700;
  }
  .testimonials {
    position: absolute; left: 0; top: 858px; width: 706px; height: 291px;
    background: var(--testimonial-bg);
  }
  .testimonials .section-title { position: absolute; left: 0; width: 698px; top: 32px; text-align: center; color: var(--ink); }
  .testimonial { position: absolute; top: 84px; width: 170px; text-align: center; }
  .portrait {
    display: block; width: 74px; height: 74px; margin: 0 auto;
    border-radius: 50%; background: radial-gradient(circle at 50% 40%, #8a8b8e, var(--portrait) 70%);
  }
  .quote {
    margin-top: 20px; font-family: "Libre Baskerville", serif; font-style: italic;
    font-size: 10.4px; line-height: 13.8px; color: var(--ink);
  }
  .author {
    margin-top: 3px; font-family: "Libre Baskerville", serif; font-style: italic;
    font-size: 10.4px; color: var(--ink); padding-right: 18px;
  }
  .footer {
    position: absolute; left: 0; top: 1149px; width: 706px; height: 51px;
    background: var(--footer-bg);
  }
  .footer-nav a { top: 18px; color: var(--white); }
</style>
</head>
<body>
  <header class="hero">
    <div class="hero-scene" role="img" aria-label="Misty photograph of a bare tree in fog"></div>

    <div class="brand">
      <span class="brand-mark"></span>
      <div class="brand-name">TRUMBO &amp; KESSLER</div>
      <div class="brand-est">EST. 1851</div>
    </div>

    <div class="nav-rule left"></div>
    <div class="nav-rule right"></div>
    <nav class="nav top-nav">
      <a href="#" style="left:217px">HOME</a>
      <a href="#" style="left:289px">ABOUT</a>
      <a href="#" style="left:365px">CONTACT</a>
      <a href="#" style="left:486px">BUY</a>
    </nav>

    <h1 class="hero-title">A PUGET SOUND ORGINAL</h1>

    <form class="enquiry">
      <h2 class="enquiry-title">MAKE <span>AN ENQUIRY</span></h2>
      <label class="field-label" style="left:29px;top:52px">Name</label>
      <input class="field" type="text" style="left:29px;top:68px;width:191px;height:23px">
      <label class="field-label" style="left:30px;top:96px">Email</label>
      <input class="field" type="email" style="left:30px;top:112px;width:195px;height:23px">
      <label class="field-label" style="left:31px;top:139px">Message</label>
      <textarea class="field" style="left:32px;top:157px;width:194px;height:74px;resize:none"></textarea>
      <button class="submit" type="button">SUBMIT</button>
    </form>
  </header>

  <section class="about">
    <h2 class="section-title">ABOUT TRUMBO AND KESSLER</h2>
    <p class="about-text">Lorem ipsum dolor sit amet, consectetur adipiscing elit, sed do eiusmod tempor incididunt ut labore et dolore magna aliqua. Ut enim ad minim veniam, quis nostrud exercitation ullamco laboris nisi ut aliquip ex ea commodo consequat. Duis aute irure dolor in reprehenderit in voluptate velit esse cillum dolore eu fugiat nulla pariatur. Excepteur sint occaecat cupidatat non proident, sunt in culpa qui officia deserunt mollit anim id est laborum.</p>
  </section>

  <section class="testimonials">
    <h2 class="section-title">TESTIMONIALS</h2>
    <article class="testimonial" style="left:69px">
      <span class="portrait" role="img" aria-label="Black and white portrait photograph of a customer"></span>
      <p class="quote">Lorem ipsum dolor sit amet, consectetur adipiscing elit, sed do eiusmod tempor incididunt ut labore et dolore magna aliqua.</p>
      <p class="author">John Example</p>
    </article>
    <article class="testimonial" style="left:259px">
      <span class="portrait" role="img" aria-label="Black and white portrait photograph of a customer"></span>
      <p class="quote">Lorem ipsum dolor sit amet, consectetur adipiscing elit, sed do eiusmod tempor incididunt ut labore et dolore magna aliqua.</p>
      <p class="author">John Example</p>
    </article>
    <article class="testimonial" style="left:454px">
      <span class="portrait" role="img" aria-label="Black and white portrait photograph of a customer"></span>
      <p class="quote">Lorem ipsum dolor sit amet, consectetur adipiscing elit, sed do eiusmod tempor incididunt ut labore et dolore magna aliqua.</p>
      <p class="author">John Example</p>
    </article>
  </section>

  <footer class="footer">
    <nav class="nav footer-nav">
      <a href="#" style="left:206px">HOME</a>
      <a href="#" style="left:277px">ABOUT</a>
      <a href="#" style="left:354px">CONTACT</a>
      <a href="#" style="left:474px">BUY</a>
    </nav>
  </footer>
</body>
</html>
```